Cybersecurity Start-Up - Veloriq

We need a MS Word Template for everyday documents. This would be leveraged to create reports, marketing materials, internal memos etc.

The document should follow the standard MS Word template format and have an H1,H2,H3, paragraph, Title, bold font, regular font, table etc. All editable with normal MS Word features.

Our logo is also attached. We would like to see the same color scheme used throughout the document. Additional attached is a sample word document that outlines all of the components we would like to see in the template.

Requirements
Must have
• - Submission must meet all standard MS Word Template requirements.
• - Submission should make use of Built in MS Styles so as the user of the template I should be able to create a brand new page and insert an H1 for example and be able to select from the styles drop down the same font/color/style that you have designed for your submission.
• - All sections in the provided document need to be contained in your submission.
• - The table of contents should auto update if I add a new page, heading, section etc.
• - Need to read and understand all of my comments which I have placed in the sample document uploaded to the briefing
Should not have
• no fixed textboxes or image boxes. everything needs to be smoothly editable in MS Word. "Editable" means more than just being able to alter text.

```html
<!DOCTYPE html>
<html lang="en">
<head>
<meta charset="utf-8">
<title>Veloriq Document Template</title>
<link href="https://fonts.googleapis.com/css2?family=Open+Sans:wght@300;400;600;700&display=swap" rel="stylesheet">
<style>
:root{
  --backdrop:#c9d3d2;
  --paper:#ffffff;
  --brand-red:#ff3d17;
  --brand-orange:#ff8a00;
  --brand-amber:#ffb000;
  --brand-yellow:#ffd34d;
  --brand-pink:#ffd6e3;
  --low-green:#8ee03a;
  --navy:#1e2b4d;
  --ink:#2b2b2b;
  --grey-row:#d9dcdf;
  --grey-line:#b9bec4;
}
*{box-sizing:border-box;margin:0;padding:0}
html,body{width:1200px;height:1200px;overflow:hidden}
body{background:var(--backdrop);font-family:"Open Sans",Arial,sans-serif;color:var(--ink);position:relative}
.page{position:absolute;width:232px;height:328px;background:var(--paper);box-shadow:2px 3px 6px rgba(0,0,0,.28);overflow:hidden}
.abs{position:absolute}
.wordmark{font-weight:700;color:var(--navy);letter-spacing:-.2px;line-height:1}
.page-head{position:absolute;left:26px;right:26px;top:16px;height:19px;border-top:1px dotted var(--brand-red);border-bottom:1px dotted var(--brand-red);text-align:center;font-weight:400;font-size:7.4px;line-height:17px;color:#222;letter-spacing:.1px}
.body-text{position:absolute;left:26px;right:22px;font-size:3.6px;line-height:4.9px;color:#333}
.h2{position:absolute;font-weight:600;font-size:5.2px;color:var(--brand-red)}
.h2.dark{color:#333;font-size:5.8px}
.footer{position:absolute;left:0;right:0;bottom:10px;height:8px}
.footer .band{position:absolute;left:0;top:1px;width:150px;height:6px;background:var(--brand-red);clip-path:polygon(0 0,100% 0,97% 100%,0 100%)}
.footer .band span{position:absolute;left:22px;top:0;font-size:3px;line-height:6px;color:#fff;letter-spacing:.1px}
.footer .wordmark{position:absolute;left:158px;top:-1px;font-size:9px}
.footer .num{position:absolute;left:206px;top:1px;width:26px;height:6px;background:var(--brand-orange);font-size:3.6px;line-height:6px;font-weight:700;text-align:center;color:#3a1a00}
/* tables */
.tbl{position:absolute;border-collapse:collapse;font-size:3px;line-height:3.6px}
.bar-head{position:absolute;height:5px;font-size:3px;line-height:5px;color:#fff;padding-left:4px;font-weight:600}
/* severity */
.sev{position:absolute;left:26px;right:22px;height:22px}
.sev .mark{position:absolute;left:0;top:1px;width:14px;height:10px;background:repeating-linear-gradient(90deg,var(--c) 0 1.6px,transparent 1.6px 2.8px)}
.sev .shield{position:absolute;left:2px;top:1px;width:11px;height:11px;border-radius:50% 50% 50% 50%/40% 40% 60% 60%;border:1.6px solid var(--c);background:#fff}
.sev .shield::after{content:"";position:absolute;left:2.4px;top:2.4px;width:3px;height:3px;border-radius:50%;background:var(--c)}
.sev .label{position:absolute;left:22px;top:0;font-size:4px;font-style:italic;color:var(--c)}
.sev .txt{position:absolute;left:22px;top:4.6px;right:0;font-size:3.5px;line-height:4.4px;color:#333}
.summary-row{position:absolute;left:26px;width:186px;height:3.6px;font-size:2.8px;line-height:3.6px}
.summary-row .name{position:absolute;left:0;width:145px;height:3.2px;background:var(--grey-row);padding-left:3px}
.summary-row .level{position:absolute;left:147px;width:39px;height:3.2px;padding-left:2px;color:#fff}
/* findings grid */
.grid{position:absolute;left:26px;top:55px;width:186px;height:236px;border:1px solid var(--g)}
.grid .v{position:absolute;left:92px;top:0;bottom:0;width:1px;background:var(--g)}
.grid .h{position:absolute;left:0;right:0;height:1px;background:var(--g)}
.findings-label{position:absolute;left:26px;top:42px;font-size:5.6px;font-weight:600}
.findings-label i{display:inline-block;width:14px;height:5px;margin-right:3px;vertical-align:-0.5px;background:repeating-linear-gradient(90deg,var(--g) 0 1.5px,transparent 1.5px 2.7px)}
/* contact */
.contact{position:absolute;font-size:2.8px;line-height:4px;color:#444}
.contact .ico{display:inline-block;width:3px;height:3px;border-radius:50%;background:var(--brand-red);margin-right:2px;vertical-align:-0.3px}
</style>
</head>
<body>

<!-- Row 1 -->
<section class="page" style="left:61px;top:66px">
  <div class="abs" role="img" aria-label="Geometric pattern of orange and red triangles" style="left:0;top:0;width:84px;height:328px;background:linear-gradient(160deg,var(--brand-orange),var(--brand-red) 55%,var(--brand-orange))"></div>
  <div class="wordmark abs" style="left:96px;top:38px;font-size:19px">Veloriq</div>
  <div class="abs" style="left:91px;top:254px;font-size:8.6px;font-weight:300;line-height:13.5px;color:var(--brand-red)">LOREM IPSUM IS SIMPLY<br>DUMMY HAS BEEN</div>
  <div class="abs" style="left:91px;top:292px;font-size:6px;color:#222">9 July 2018</div>
</section>

<section class="page" style="left:348px;top:66px">
  <div class="wordmark abs" style="left:0;right:0;top:44px;text-align:center;font-size:19px">Veloriq</div>
  <svg class="abs" style="left:0;top:120px" width="232" height="208" viewBox="0 0 232 208">
    <path d="M0 30 Q116 -18 232 30 L232 208 L0 208 Z" fill="var(--brand-red)"/>
    <path d="M0 25 Q116 -26 232 25" fill="none" stroke="var(--brand-red)" stroke-width="1.6"/>
  </svg>
  <div class="abs" style="left:0;right:0;top:186px;text-align:center;font-size:10px;font-weight:300;line-height:17px;color:#fff">LOREM IPSUM IS SIMPLY<br>DUMMY HAS BEEN</div>
  <div class="abs" style="left:0;right:0;top:232px;text-align:center;font-size:4.6px;font-weight:600;color:#fff">9 July 2018</div>
</section>

<section class="page" style="left:634px;top:66px">
  <div class="page-head">TABLE OF CONTENTS</div>
  <div class="h2" style="left:26px;top:47px;font-size:6px">Contents</div>
  <div class="abs" style="left:26px;top:62px;width:186px;font-size:3.6px;line-height:7.9px;color:#333">
    <div style="display:flex"><span>Table of Contents</span><span style="flex:1;border-bottom:1px dotted #999;margin:0 3px 3px"></span><span>01</span></div>
    <div style="display:flex"><span>Executive Summary</span><span style="flex:1;border-bottom:1px dotted #999;margin:0 3px 3px"></span><span>02</span></div>
    <div style="display:flex"><span>Our Understanding of Your Needs</span><span style="flex:1;border-bottom:1px dotted #999;margin:0 3px 3px"></span><span>02</span></div>
    <div style="display:flex"><span>Our Recommendations</span><span style="flex:1;border-bottom:1px dotted #999;margin:0 3px 3px"></span><span>03</span></div>
    <div style="display:flex"><span>Our Approach</span><span style="flex:1;border-bottom:1px dotted #999;margin:0 3px 3px"></span><span>05</span></div>
    <div style="display:flex"><span>Budget and Timeframe</span><span style="flex:1;border-bottom:1px dotted #999;margin:0 3px 3px"></span><span>07</span></div>
    <div style="display:flex"><span>Appendix A: About Pine Hollow</span><span style="flex:1;border-bottom:1px dotted #999;margin:0 3px 3px"></span><span>10</span></div>
    <div style="display:flex"><span>Appendix B: Selected Client List</span><span style="flex:1;border-bottom:1px dotted #999;margin:0 3px 3px"></span><span>10</span></div>
    <div style="display:flex"><span>Appendix C: Our Capabilities</span><span style="flex:1;border-bottom:1px dotted #999;margin:0 3px 3px"></span><span>11</span></div>
    <div style="display:flex"><span>Appendix D: Our Process</span><span style="flex:1;border-bottom:1px dotted #999;margin:0 3px 3px"></span><span>12</span></div>
  </div>
  <div class="footer"><div class="band"><span>IN-COMMERCIAL-CONFIDENCE</span></div><div class="wordmark">Veloriq</div><div class="num">01</div></div>
</section>

<section class="page" style="left:907px;top:66px">
  <div class="page-head">HEADLINE HERE</div>
  <div class="h2 dark" style="left:23px;top:41px">Solution</div>
  <div class="body-text" style="left:23px;top:50px">Ledgerly builds automation in stages on top of its current system to reach full automation. Ledgerly automates every manual task performed by the user. It starts by connecting to all sources of accounting data such as bank accounts, credit cards and document storage. Based on these data, Ledgerly creates bookings and generates financial reports.</div>
  <div class="h2 dark" style="left:23px;top:86px">Professional Outcomes</div>
  <div class="bar-head" style="left:23px;top:96px;width:185px;background:var(--brand-orange)">Work Roles – Table 1</div>
  <div class="abs" style="left:23px;top:102px;width:185px;font-size:2.9px;color:#fff">
    <div style="display:flex;height:6px;margin-bottom:1px"><span style="width:57px;background:var(--brand-pink);color:var(--brand-red);padding-left:3px;line-height:6px">Work Role Name</span><span style="flex:1;margin-left:1px;background:var(--brand-pink)"></span></div>
    <div style="display:flex;height:6px;margin-bottom:1px"><span style="width:57px;background:var(--brand-yellow);padding-left:3px;line-height:6px">Specialty Area</span><span style="flex:1;margin-left:1px;background:var(--brand-yellow)"></span></div>
    <div style="display:flex;height:6px;margin-bottom:1px"><span style="width:57px;background:var(--brand-pink);color:var(--brand-red);padding-left:3px;line-height:6px">CSF Category</span><span style="flex:1;margin-left:1px;background:var(--brand-pink)"></span></div>
    <div style="display:flex;height:6px;margin-bottom:1px"><span style="width:57px;background:var(--brand-yellow);padding-left:3px;line-height:6px">Work Role Description</span><span style="flex:1;margin-left:1px;background:var(--brand-yellow)"></span></div>
    <div style="display:flex;height:12px;margin-bottom:1px"><span style="width:57px;background:var(--brand-pink);color:var(--brand-red);padding-left:3px;line-height:12px">Tasks</span><span style="flex:1;margin-left:1px;background:repeating-linear-gradient(180deg,var(--brand-pink) 0 3px,#fff 3px 4px)"></span></div>
    <div style="display:flex;height:12px;margin-bottom:1px"><span style="width:57px;background:var(--brand-yellow);padding-left:3px;line-height:12px">Skills</span><span style="flex:1;margin-left:1px;background:repeating-linear-gradient(180deg,var(--brand-yellow) 0 3px,#fff 3px 4px)"></span></div>
    <div style="display:flex;height:12px"><span style="width:57px;background:var(--brand-pink);color:var(--brand-red);padding-left:3px;line-height:12px">Abilities</span><span style="flex:1;margin-left:1px;background:repeating-linear-gradient(180deg,var(--brand-pink) 0 3px,#fff 3px 4px)"></span></div>
  </div>
  <div class="h2 dark" style="left:25px;top:181px">Training Content</div>
  <div class="bar-head" style="left:25px;top:195px;width:183px;background:var(--brand-red)">Module 1 – Table 2</div>
  <div class="abs" style="left:25px;top:200px;width:183px;height:45px;border:1px solid var(--brand-red);border-top:0;background:repeating-linear-gradient(180deg,transparent 0 6.3px,var(--brand-red) 6.3px 7.3px)"><div class="abs" style="left:65px;top:0;bottom:0;width:1px;background:var(--brand-red)"></div></div>
  <div class="bar-head" style="left:25px;top:253px;width:183px;background:var(--brand-red)">Module 1 – Table 2</div>
  <div class="abs" style="left:25px;top:258px;width:183px;height:45px;border:1px solid var(--brand-red);border-top:0;background:repeating-linear-gradient(180deg,transparent 0 6.3px,var(--brand-red) 6.3px 7.3px)"><div class="abs" style="left:65px;top:0;bottom:0;width:1px;background:var(--brand-red)"></div></div>
  <div class="footer"><div class="band"><span>IN-COMMERCIAL-CONFIDENCE</span></div><div class="wordmark">Veloriq</div><div class="num">01</div></div>
</section>

<!-- Row 2 -->
<section class="page" style="left:61px;top:436px">
  <div class="page-head">TECHNICAL OVERVIEW</div>
  <div class="body-text" style="top:39px">Lorem ipsum dolor sit amet, consectetur adipiscing elit, sed do eiusmod tempor incididunt ut labore et dolore magna aliqua. Ut enim ad minim veniam, quis nostrud exercitation ullamco laboris nisi ut aliquip ex ea commodo consequat. Duis aute irure dolor in reprehenderit in voluptate velit esse cillum dolore.</div>
  <div class="bar-head" style="left:26px;top:66px;width:186px;background:var(--brand-orange)">Table Two</div>
  <div class="abs" style="left:26px;top:71px;width:186px;height:17px;background:linear-gradient(180deg,var(--grey-row) 0 8px,#fff 8px 9px,#eceef0 9px)"><div class="abs" style="left:93px;top:0;bottom:0;width:1px;background:#fff"></div></div>
  <div class="h2" style="left:26px;top:93px;font-size:4.4px">Severity Ratings</div>
  <div class="sev" style="top:105px;--c:#e8141b"><i class="mark"></i><span class="label">Critical</span><p class="txt">Duis aute irure dolor in reprehenderit in voluptate velit esse cillum dolore eu fugiat nulla pariatur. Excepteur sint occaecat cupidatat non proident, sunt in culpa qui officia deserunt mollit anim.</p></div>
  <div class="sev" style="top:130px;--c:#ff3d17"><i class="mark"></i><span class="label">High</span><p class="txt">Duis aute irure dolor in reprehenderit in voluptate velit esse cillum dolore eu fugiat nulla pariatur. Excepteur sint occaecat cupidatat non proident, sunt in culpa qui officia deserunt mollit anim.</p></div>
  <div class="sev" style="top:156px;--c:#ff9c00"><i class="mark"></i><span class="label">Medium</span><p class="txt">Duis aute irure dolor in reprehenderit in voluptate velit esse cillum dolore eu fugiat nulla pariatur. Excepteur sint occaecat cupidatat non proident, sunt in culpa qui officia deserunt mollit anim.</p></div>
  <div class="sev" style="top:182px;--c:#8ee03a"><i class="mark"></i><span class="label">Low</span><p class="txt">Duis aute irure dolor in reprehenderit in voluptate velit esse cillum dolore eu fugiat nulla pariatur. Excepteur sint occaecat cupidatat non proident, sunt in culpa qui officia deserunt mollit anim.</p></div>
  <div class="h2" style="left:26px;top:210px;font-size:4.4px">Summary Of Findings</div>
  <div class="body-text" style="top:217px">Duis aute irure dolor in reprehenderit in voluptate velit esse cillum dolore eu fugiat nulla pariatur. Excepteur sint occaecat cupidatat non proident, sunt in culpa qui officia.</div>
  <div class="bar-head" style="left:26px;top:240px;width:186px;background:var(--brand-orange)">Table 4</div>
  <div class="summary-row" style="top:246px"><span class="name">Finding Name</span><span class="level" style="background:var(--grey-row);color:#333">Severity</span></div>
  <div class="summary-row" style="top:250px"><span class="name">Critical Finding Title</span><span class="level" style="background:#e8141b">Critical</span></div>
  <div class="summary-row" style="top:254px"><span class="name">High Finding Title</span><span class="level" style="background:var(--brand-red)">High</span></div>
  <div class="summary-row" style="top:258px"><span class="name">Medium Finding Title</span><span class="level" style="background:var(--brand-orange)">Medium</span></div>
  <div class="summary-row" style="top:262px"><span class="name">Low Finding Title</span><span class="level" style="background:var(--low-green)">Low</span></div>
  <div class="footer"><div class="band"><span>IN-COMMERCIAL-CONFIDENCE</span></div><div class="wordmark">Veloriq</div><div class="num">01</div></div>
</section>

<section class="page" style="left:345px;top:436px">
  <div class="page-head">TECHNICAL OVERVIEW</div>
  <div class="body-text" style="top:39px">Lorem ipsum dolor sit amet, consectetur adipiscing elit, sed do eiusmod tempor incididunt ut labore et dolore magna aliqua. Ut enim ad minim veniam, quis nostrud exercitation ullamco laboris nisi ut aliquip ex ea commodo consequat. Duis aute irure dolor in reprehenderit in voluptate velit esse cillum dolore.</div>
  <div class="bar-head" style="left:26px;top:66px;width:186px;background:var(--brand-orange)">Table Two</div>
  <div class="abs" style="left:26px;top:71px;width:186px;height:17px;background:linear-gradient(180deg,var(--grey-row) 0 8px,#fff 8px 9px,#eceef0 9px)"><div class="abs" style="left:93px;top:0;bottom:0;width:1px;background:#fff"></div></div>
  <div class="h2" style="left:26px;top:93px;font-size:4.4px">Severity Ratings</div>
  <div class="sev" style="top:105px;--c:#e8141b"><i class="shield"></i><span class="label">Critical</span><p class="txt">Duis aute irure dolor in reprehenderit in voluptate velit esse cillum dolore eu fugiat nulla pariatur. Excepteur sint occaecat cupidatat non proident, sunt in culpa qui officia deserunt mollit anim.</p></div>
  <div class="sev" style="top:130px;--c:#ff3d17"><i class="shield"></i><span class="label">High</span><p class="txt">Duis aute irure dolor in reprehenderit in voluptate velit esse cillum dolore eu fugiat nulla pariatur. Excepteur sint occaecat cupidatat non proident, sunt in culpa qui officia deserunt mollit anim.</p></div>
  <div class="sev" style="top:156px;--c:#ffb000"><i class="shield"></i><span class="label">Medium</span><p class="txt">Duis aute irure dolor in reprehenderit in voluptate velit esse cillum dolore eu fugiat nulla pariatur. Excepteur sint occaecat cupidatat non proident, sunt in culpa qui officia deserunt mollit anim.</p></div>
  <div class="sev" style="top:182px;--c:#8ee03a"><i class="shield"></i><span class="label">Low</span><p class="txt">Duis aute irure dolor in reprehenderit in voluptate velit esse cillum dolore eu fugiat nulla pariatur. Excepteur sint occaecat cupidatat non proident, sunt in culpa qui officia deserunt mollit anim.</p></div>
  <div class="h2" style="left:26px;top:218px;font-size:4.4px">Summary Of Findings</div>
  <div class="body-text" style="top:225px">Duis aute irure dolor in reprehenderit in voluptate velit esse cillum dolore eu fugiat nulla pariatur. Excepteur sint occaecat cupidatat non proident, sunt in culpa qui officia.</div>
  <div class="bar-head" style="left:26px;top:248px;width:186px;background:var(--brand-orange)">Table 4</div>
  <div class="summary-row" style="top:254px"><span class="name">Finding Name</span><span class="level" style="background:var(--grey-row);color:#333">Severity</span></div>
  <div class="summary-row" style="top:258px"><span class="name">Critical Finding Title</span><span class="level" style="background:#e8141b">Critical</span></div>
  <div class="summary-row" style="top:262px"><span class="name">High Finding Title</span><span class="level" style="background:var(--brand-red)">High</span></div>
  <div class="summary-row" style="top:266px"><span class="name">Medium Finding Title</span><span class="level" style="background:var(--brand-orange)">Medium</span></div>
  <div class="summary-row" style="top:270px"><span class="name">Low Finding Title</span><span class="level" style="background:var(--low-green)">Low</span></div>
  <div class="footer"><div class="band"><span>IN-COMMERCIAL-CONFIDENCE</span></div><div class="wordmark">Veloriq</div><div class="num">01</div></div>
</section>

<section class="page" style="left:634px;top:436px;--g:#f06a7a">
  <div class="page-head">DETAILED OBSERVATIONS</div>
  <div class="findings-label" style="color:#e8141b;--g:#e8141b"><i></i>Critical Findings</div>
  <div class="grid"><div class="v"></div><div class="h" style="top:16px"></div><div class="h" style="top:66px"></div><div class="h" style="top:114px"></div><div class="h" style="top:200px"></div></div>
  <div class="footer"><div class="band"><span>IN-COMMERCIAL-CONFIDENCE</span></div><div class="wordmark">Veloriq</div><div class="num">01</div></div>
</section>

<section class="page" style="left:907px;top:436px;--g:#ffc36b">
  <div class="page-head">DETAILED OBSERVATIONS</div>
  <div class="findings-label" style="color:var(--brand-amber);--g:var(--brand-amber)"><i></i>Medium Findings</div>
  <div class="grid"><div class="v"></div><div class="h" style="top:16px"></div><div class="h" style="top:66px"></div><div class="h" style="top:114px"></div><div class="h" style="top:200px"></div></div>
  <div class="footer"><div class="band"><span>IN-COMMERCIAL-CONFIDENCE</span></div><div class="wordmark">Veloriq</div><div class="num">01</div></div>
</section>

<!-- Row 3 -->
<section class="page" style="left:61px;top:806px">
  <div class="abs" style="left:26px;right:22px;top:21px;font-size:7.2px;color:#222;padding-bottom:2px;border-bottom:1px dotted var(--brand-red)">APPENDIX 01 – ENGAGEMENT METHODOLOGY</div>
  <div class="body-text" style="top:40px">Lorem ipsum dolor sit amet, consectetur adipiscing elit, sed do eiusmod tempor incididunt ut labore et dolore magna aliqua. Ut enim ad minim veniam, quis nostrud exercitation ullamco laboris nisi ut aliquip ex ea commodo consequat. Duis aute irure dolor in reprehenderit in voluptate velit esse cillum dolore.</div>
  <div class="footer"><div class="band"><span>IN-COMMERCIAL-CONFIDENCE</span></div><div class="wordmark">Veloriq</div><div class="num">01</div></div>
</section>

<section class="page" style="left:345px;top:806px">
  <div class="abs" role="img" aria-label="Soft pattern of pale pink and peach triangles" style="left:0;top:0;width:128px;height:328px;background:linear-gradient(165deg,#fde3d6,#fad7e6 45%,#f6d2e8 70%,#fce6e4)"></div>
  <div class="wordmark abs" style="left:38px;top:288px;font-size:9px">Veloriq</div>
  <div class="contact" style="left:94px;top:285px"><span class="ico"></span>000-555-0142 ext 200<br><span class="ico"></span>contact@veloriq-mail.test<br><span class="ico"></span>www.veloriq-site.test</div>
  <div class="contact" style="left:145px;top:285px;border-left:1px solid #bbb;padding-left:4px">Suite 40, 18 Harbor Row<br>Northgate, Westland</div>
</section>

<section class="page" style="left:634px;top:806px">
  <svg class="abs" style="left:0;top:0" width="232" height="200" viewBox="0 0 232 200">
    <path d="M0 0 H232 V160 Q116 208 0 160 Z" fill="var(--brand-red)"/>
    <path d="M0 166 Q116 214 232 166" fill="none" stroke="var(--brand-red)" stroke-width="1.6"/>
  </svg>
  <div class="wordmark abs" style="left:37px;top:290px;font-size:9px">Veloriq</div>
  <div class="contact" style="left:93px;top:287px"><span class="ico"></span>000-555-0142 ext 200<br><span class="ico"></span>contact@veloriq-mail.test<br><span class="ico"></span>www.veloriq-site.test</div>
  <div class="contact" style="left:144px;top:287px;border-left:1px solid #bbb;padding-left:4px">Suite 40, 18 Harbor Row<br>Northgate, Westland</div>
</section>

</body>
</html>
```